I need a great, modern, professional website for my paint contracting company, Ashbrook Coating Contractors, LLC. I have many good pix that can be used from jobs completed that would be attractive. We do commercial, residential and industrial jobs. I’m fully insured and licensed, including holding a General Contractor’s License as a Subcontractor. I know nothing about coding websites. I’ll have my assistant get on tomorrow and learn how to drop files. I’m not sure what files to send. This will be difficult at best, it being able to talk this through. Oh well. What’s next?

Target Market(s)

General Contractors

Industry/Entity Type

Paint Contracting

Coding

Coded - Design and coding required

Font styles to use
Sans Serif

Colors
00AB8E
00BBA5
67D7C9
C6EFE9
E9F9F6

Requirements
Must have
• Pix of completed jobs, bio, maybe testimonials from happy customers? ….
Nice to have
• I’d like it to have a modern appeal, but still have some warmth.
Should not have
• ??

```html
<!DOCTYPE html>
<html lang="en">
<head>
<meta charset="utf-8">
<title>Ashbrook Coating Contractors, LLC</title>
<link rel="stylesheet" href="https://fonts.googleapis.com/css2?family=Poppins:wght@500;600;700&family=Roboto:wght@400;500;700&display=swap">
<style>
:root{
  --green:#00AB8E;
  --teal:#00BBA5;
  --mint:#67D7C9;
  --pale:#C6EFE9;
  --wash:#E9F9F6;
  --ink:#1d1d1d;
  --grey:#6b6b6b;
  --black:#0b0b0b;
  --white:#ffffff;
}
*{margin:0;padding:0;box-sizing:border-box}
html,body{width:1200px;height:4488px;overflow:hidden;background:var(--white)}
body{font-family:"Roboto",Arial,sans-serif;color:var(--ink);position:relative}
.head-font{font-family:"Poppins",Arial,sans-serif}
section,header,footer{position:absolute;left:0;width:1200px}

/* header */
.site-header{top:0;height:105px;background:var(--white);z-index:3}
.brand{position:absolute;left:49px;top:18px;font-family:"Poppins",sans-serif;font-weight:700;font-size:28px;line-height:35px;color:var(--green)}
.socials{position:absolute;left:560px;top:18px;display:flex;gap:14px}
.socials span{width:28px;height:28px;border:2px solid var(--green);border-radius:50%}
.quote-btn{position:absolute;left:749px;top:14px;width:136px;height:38px;background:var(--green);color:var(--white);font:700 13px "Roboto",sans-serif;display:flex;align-items:center;justify-content:center;gap:8px;border-radius:3px}
.nav-bar{position:absolute;left:322px;top:63px;width:660px;height:42px;background:var(--green);clip-path:polygon(30px 0,100% 0,100% 100%,0 100%);display:flex;align-items:center;padding-left:40px;gap:24px}
.nav-bar a{color:var(--white);font-size:14px;text-decoration:none}
.nav-bar a.active{font-weight:700}
.call-box{position:absolute;right:0;top:0;width:262px;height:105px;background:var(--green);clip-path:polygon(24px 0,100% 0,100% 100%,0 100%);color:var(--white)}
.call-icon{position:absolute;left:34px;top:36px;width:38px;height:38px;border-radius:50%;background:rgba(255,255,255,.25);display:flex;align-items:center;justify-content:center}
.call-box small{position:absolute;left:88px;top:30px;font-size:12px;font-weight:500}
.call-box strong{position:absolute;left:88px;top:52px;font-size:20px;font-weight:700}

/* hero */
.hero{top:105px;height:602px;background:linear-gradient(100deg,#f3eef0 0%,#f6dcd9 45%,#efb4ae 75%,#f0c9b8 100%)}
.hero-photo{position:absolute;inset:0}
.hero-text{position:absolute;left:108px;top:180px}
.hero-text .kicker{font-family:"Poppins",sans-serif;color:var(--green);font-weight:600;font-size:27px}
.hero-text h1{font-family:"Poppins",sans-serif;font-weight:700;font-size:44px;line-height:45px;margin-top:12px;color:#2a2a2a}
.hero-text p{margin-top:20px;width:370px;font-size:14.5px;line-height:26px;color:#222}
.btn{display:inline-flex;align-items:center;gap:8px;font-weight:700;font-size:14px;border-radius:3px}
.btn-solid{background:var(--green);color:var(--white);height:47px;padding:0 20px;margin-top:24px}

/* about */
.about{top:707px;height:626px}
.hex-frame{position:absolute;left:113px;top:86px;width:392px;height:452px;background:var(--white);clip-path:polygon(50% 0,100% 25%,100% 75%,50% 100%,0 75%,0 25%);filter:drop-shadow(0 0 14px rgba(0,0,0,.15))}
.hex-photo{position:absolute;left:125px;top:100px;width:368px;height:424px;clip-path:polygon(50% 0,100% 25%,100% 75%,50% 100%,0 75%,0 25%);background:linear-gradient(120deg,#d9d6cc,#cfc39a 55%,#e8c45f)}
.about-text{position:absolute;left:598px;top:141px;width:486px}
.rule{width:56px;height:3px;background:var(--green)}
.about-text h2{font-family:"Poppins",sans-serif;font-weight:600;font-size:35px;line-height:41px;margin-top:28px}
.about-text p{font-size:14.5px;line-height:25px;color:var(--grey);margin-top:18px;text-align:justify}
.btn-outline{border:2px solid var(--green);color:var(--green);height:44px;padding:0 20px;margin-top:18px}

/* services */
.services{top:1333px;height:640px;background:linear-gradient(180deg,var(--wash),var(--pale) 60%,var(--wash))}
.sec-title{position:absolute;left:0;width:100%;text-align:center;font-family:"Poppins",sans-serif;font-weight:600;font-size:35px}
.sec-title::after{content:"";display:block;width:90px;height:4px;background:var(--green);margin:10px auto 0}
.card{position:absolute;top:156px;width:324px;height:406px}
.card-photo{position:absolute;left:0;top:0;width:324px;height:236px}
.card-body{position:absolute;left:9px;top:183px;width:306px;height:223px;background:var(--white);border-radius:150px 150px 4px 4px/40px 40px 4px 4px;box-shadow:0 6px 14px rgba(0,0,0,.08);text-align:center;border-top:3px solid var(--green)}
.card-icon{position:absolute;left:50%;top:-34px;transform:translateX(-50%);width:64px;height:64px;border-radius:50%;background:var(--white);display:flex;align-items:center;justify-content:center;box-shadow:0 2px 8px rgba(0,0,0,.1)}
.card-body h3{margin-top:56px;font-family:"Poppins",sans-serif;font-size:16px;font-weight:600}
.card-body p{margin:18px auto 0;width:260px;font-size:14px;line-height:26px;color:var(--grey)}
.card-body .more{margin-top:10px;color:var(--green);font-weight:500;font-size:14px;display:inline-flex;gap:10px;align-items:center}

/* banner */
.licence{top:1973px;height:274px;background:linear-gradient(90deg,var(--green),var(--teal) 50%,var(--green));display:flex;align-items:center;justify-content:center}
.licence p{font-family:"Poppins",sans-serif;font-weight:600;font-size:34px;line-height:49px;color:var(--white);text-align:center}

/* gallery */
.gallery{top:2247px;height:816px}
.tile{position:absolute}

/* team */
.team{top:3063px;height:536px;background:linear-gradient(180deg,var(--teal),var(--green))}
.team .sec-title{color:var(--white)}
.team .sec-title::after{background:var(--white)}
.member{position:absolute;top:191px;width:240px;text-align:center;color:var(--white)}
.avatar{width:164px;height:164px;margin:0 auto;border-radius:50%;border:3px solid var(--white);padding:6px}
.avatar div{width:100%;height:100%;border-radius:50%;background:linear-gradient(160deg,#e9ecef,#c9ced3)}
.member h4{margin-top:26px;font-family:"Poppins",sans-serif;font-size:16px;font-weight:600}
.member p{margin-top:10px;font-size:14px;line-height:24px}

/* testimonials */
.customers{top:3599px;height:498px}
.review{position:absolute;top:176px;width:422px;height:205px;background:var(--white);box-shadow:0 4px 18px rgba(0,0,0,.1);padding:22px 20px}
.stars{color:#f4c20d;font-size:15px;letter-spacing:4px}
.review p{margin-top:14px;font-size:14.5px;line-height:26px;color:var(--grey)}
.review h5{margin-top:14px;font-size:14px;font-weight:500}
.review .mark{position:absolute;right:20px;bottom:0;font-family:"Poppins",sans-serif;font-size:92px;line-height:60px;color:#e6e6e6;height:50px;overflow:hidden}
.review .face{position:absolute;left:16px;bottom:-35px;width:70px;height:70px;border-radius:50%;background:linear-gradient(160deg,#b9c2c9,#7d8a94);border:3px solid var(--white)}

/* footer */
.site-footer{top:4097px;height:391px;background:var(--black);color:var(--white)}
.f-col{position:absolute;top:70px}
.f-col h6{font-family:"Poppins",sans-serif;font-size:15px;font-weight:600}
.f-col ul{list-style:none;margin-top:20px}
.f-col li{font-size:13.5px;line-height:28px}
.contact-item{display:flex;gap:10px;margin-top:18px;font-size:12.5px;line-height:18px}
.contact-item b{display:block;font-weight:700}
.f-quote{display:inline-flex;align-items:center;justify-content:center;width:193px;height:42px;background:var(--green);font-weight:700;font-size:14px;margin-top:24px;border-radius:3px}
.f-line{position:absolute;left:110px;top:315px;width:980px;height:1px;background:#333}
.to-top{position:absolute;left:1110px;top:276px;width:34px;height:34px;border-radius:50%;background:var(--green);display:flex;align-items:center;justify-content:center}
.copyright{position:absolute;top:346px;width:100%;text-align:center;font-size:13px}
</style>
</head>
<body>

<header class="site-header">
  <div class="brand">Ashbrook Coating<br>Contractors, LLC</div>
  <div class="socials"><span></span><span></span><span></span><span></span></div>
  <div class="quote-btn">GET A QUOTE
    <svg width="13" height="13" viewBox="0 0 14 14"><circle cx="7" cy="7" r="7" fill="#fff"/><path d="M5.5 4l3 3-3 3" stroke="#00AB8E" stroke-width="2" fill="none"/></svg>
  </div>
  <nav class="nav-bar">
    <a class="active">Home</a><a>About Us</a><a>Services</a><a>Gallery</a><a>Team</a><a>Testimonial</a><a>Contact Us</a>
  </nav>
  <div class="call-box">
    <div class="call-icon"><svg width="20" height="20" viewBox="0 0 24 24"><path d="M6.6 10.8a15 15 0 006.6 6.6l2.2-2.2c.3-.3.7-.4 1-.2 1.1.4 2.3.6 3.6.6.6 0 1 .4 1 1V20c0 .6-.4 1-1 1A17 17 0 013 4c0-.6.4-1 1-1h3.5c.6 0 1 .4 1 1 0 1.3.2 2.5.6 3.6.1.3 0 .7-.2 1z" fill="#fff"/></svg></div>
    <small>Call Us Today</small>
    <strong>+1 888 888 8888</strong>
  </div>
</header>

<section class="hero">
  <div class="hero-photo" role="img" aria-label="Painters at work: one pouring orange paint into a tray, another rolling a pink wall"></div>
  <div class="hero-text">
    <div class="kicker">Welcome to</div>
    <h1>Ashbrook Coating<br>Contractors</h1>
    <p>Lorem ipsum dolor sit ame, consectetur adipiscing iusm tempor incididunt ut labore et dolore magna.</p>
    <span class="btn btn-solid">GET STARTED
      <svg width="13" height="13" viewBox="0 0 14 14"><circle cx="7" cy="7" r="7" fill="#fff"/><path d="M5.5 4l3 3-3 3" stroke="#00AB8E" stroke-width="2" fill="none"/></svg>
    </span>
  </div>
</section>

<section class="about">
  <div class="hex-frame"></div>
  <div class="hex-photo" role="img" aria-label="Painter on a rope harness rolling yellow paint onto a building wall"></div>
  <div class="about-text">
    <div class="rule"></div>
    <h2>About Ashbrook Coating Contractors</h2>
    <p>Lorem ipsum dolor sit amet, consectetur adipiscing elit sed eiusmod tempor incididunt ut labore et dolore magna aliqua Ut enim ad minim veniam, quis nostrud exercitation ullamco laboris nisi ut aliquip ex ea commodo consequat. Duis aute irure dolor in reprehenderit in voluptate velit esse cillum dolore eu fugiat nulla pariatur. ExcepteLorem ipsum dolor sit amet, consectetur adipiscing elit, sed do eiusmod tempor incididunt ut labore et dolore magna aliqua. Ut enim ad minim</p>
    <span class="btn btn-outline">LEARN MORE
      <svg width="13" height="13" viewBox="0 0 14 14"><circle cx="7" cy="7" r="7" fill="#00AB8E"/><path d="M5.5 4l3 3-3 3" stroke="#fff" stroke-width="2" fill="none"/></svg>
    </span>
  </div>
</section>

<section class="services">
  <h2 class="sec-title" style="top:60px">Our Services</h2>

  <div class="card" style="left:96px">
    <div class="card-photo" role="img" aria-label="Workers in hi-vis vests painting a commercial interior" style="background:linear-gradient(160deg,#e6e4dc,#b9b6a8)"></div>
    <div class="card-body">
      <div class="card-icon"><svg width="34" height="34" viewBox="0 0 34 34" fill="none" stroke="#00AB8E" stroke-width="2"><rect x="4" y="12" width="10" height="18"/><rect x="14" y="5" width="16" height="25"/><path d="M18 10h3M24 10h3M18 16h3M24 16h3M18 22h3M24 22h3M7 17h4M7 23h4"/></svg></div>
      <h3>Commercial</h3>
      <p>Lorem ipsum dolor amet consectetur adipiscinsed eiusmoded incididunted labored dolore magna aliquad.</p>
      <span class="more">LEARN MOR <svg width="13" height="13" viewBox="0 0 14 14"><circle cx="7" cy="7" r="7" fill="#00AB8E"/><path d="M5.5 4l3 3-3 3" stroke="#fff" stroke-width="2" fill="none"/></svg></span>
    </div>
  </div>

  <div class="card" style="left:439px">
    <div class="card-photo" role="img" aria-label="Woman painting a home interior with a roller" style="background:linear-gradient(160deg,#eef1f3,#7fa6c4)"></div>
    <div class="card-body">
      <div class="card-icon"><svg width="34" height="34" viewBox="0 0 34 34" fill="none" stroke="#00AB8E" stroke-width="2"><path d="M5 15L17 5l12 10M9 12v16h16V12"/><rect x="13" y="17" width="8" height="5"/><path d="M17 22v6"/></svg></div>
      <h3>Residential</h3>
      <p>Lorem ipsum dolor amet consectetur adipiscinsed eiusmoded incididunted labored dolore magna aliquad.</p>
      <span class="more">LEARN MOR <svg width="13" height="13" viewBox="0 0 14 14"><circle cx="7" cy="7" r="7" fill="#00AB8E"/><path d="M5.5 4l3 3-3 3" stroke="#fff" stroke-width="2" fill="none"/></svg></span>
    </div>
  </div>

  <div class="card" style="left:782px">
    <div class="card-photo" role="img" aria-label="Worker spray-coating blue steel panels in an industrial yard" style="background:linear-gradient(160deg,#7d8790,#2f5fa8)"></div>
    <div class="card-body">
      <div class="card-icon"><svg width="34" height="34" viewBox="0 0 34 34" fill="none" stroke="#00AB8E" stroke-width="2"><path d="M4 30V16l7 4v-4l7 4v-4l7 4V8h5v22z"/><circle cx="23" cy="9" r="4"/></svg></div>
      <h3>Industrial</h3>
      <p>Lorem ipsum dolor amet consectetur adipiscinsed eiusmoded incididunted labored dolore magna aliquad.</p>
      <span class="more">LEARN MOR <svg width="13" height="13" viewBox="0 0 14 14"><circle cx="7" cy="7" r="7" fill="#00AB8E"/><path d="M5.5 4l3 3-3 3" stroke="#fff" stroke-width="2" fill="none"/></svg></span>
    </div>
  </div>
</section>

<section class="licence">
  <p>we are fully insured and licensed,<br>including holding a General Contractor’s<br>License as a Subcontractor.</p>
</section>

<section class="gallery">
  <h2 class="sec-title" style="top:88px">Our Gallery</h2>
  <div class="tile" style="left:111px;top:187px;width:483px;height:278px;background:linear-gradient(135deg,#2f4a5c,#d8dde0 45%,#eef0f1)" role="img" aria-label="Finished open-plan office with blue feature wall"></div>
  <div class="tile" style="left:604px;top:187px;width:485px;height:278px;background:linear-gradient(135deg,#f1ede6,#cfb391 55%,#efe9e0)" role="img" aria-label="Bright living room with wood panelling"></div>
  <div class="tile" style="left:113px;top:476px;width:322px;height:252px;background:linear-gradient(180deg,#6c86a3,#b9c6d2 45%,#4d4a43 75%,#4d6a3e)" role="img" aria-label="Modern two-storey house exterior at dusk"></div>
  <div class="tile" style="left:446px;top:476px;width:310px;height:252px;background:linear-gradient(135deg,#f2f2f0,#c9c6c0)" role="img" aria-label="White living room with grey sofa"></div>
  <div class="tile" style="left:766px;top:476px;width:321px;height:252px;background:linear-gradient(135deg,#6a4a38,#a8664e 45%,#d3d6d6)" role="img" aria-label="Loft office with exposed brick wall"></div>
</section>

<section class="team">
  <h2 class="sec-title" style="top:60px">Our Team</h2>
  <div class="member" style="left:92px"><div class="avatar"><div role="img" aria-label="Team member portrait"></div></div><h4>Jhone Deo</h4><p>Lorem ipsum dolor consectetur<br>adipiscing elit sed do eiusmod</p></div>
  <div class="member" style="left:350px"><div class="avatar"><div role="img" aria-label="Team member portrait"></div></div><h4>Jhone Deo</h4><p>Lorem ipsum dolor consectetur<br>adipiscing elit sed do eiusmod</p></div>
  <div class="member" style="left:608px"><div class="avatar"><div role="img" aria-label="Team member portrait"></div></div><h4>Jhone Deo</h4><p>Lorem ipsum dolor consectetur<br>adipiscing elit sed do eiusmod</p></div>
  <div class="member" style="left:868px"><div class="avatar"><div role="img" aria-label="Team member portrait"></div></div><h4>Jhone Deo</h4><p>Lorem ipsum dolor consectetur<br>adipiscing elit sed do eiusmod</p></div>
</section>

<section class="customers">
  <h2 class="sec-title" style="top:80px">Happy Customers</h2>
  <div class="review" style="left:153px">
    <div class="stars">★★★★★</div>
    <p>Lorem ipsum dolor sit ameed consectetur adipiscing elitsed do eiusmod tempor incididunte uted labore et dolore magna aliquad Uted enim ad minim veniam.</p>
    <h5>Jhon Doe</h5>
    <div class="mark">“</div>
    <div class="face" role="img" aria-label="Customer portrait"></div>
  </div>
  <div class="review" style="left:624px">
    <div class="stars">★★★★★</div>
    <p>Lorem ipsum dolor sit ameed consectetur adipiscing elitsed do eiusmod tempor incididunte uted labore et dolore magna aliquad Uted enim ad minim veniam.</p>
    <h5>Jhon Doe</h5>
    <div class="mark">“</div>
    <div class="face" role="img" aria-label="Customer portrait"></div>
  </div>
</section>

<footer class="site-footer">
  <div class="f-col" style="left:110px"><h6>Quick Links</h6>
    <ul><li>Home</li><li>About</li><li>Services</li><li>Gallery</li><li>Team</li><li>Testimonial</li><li>Contact Us</li></ul></div>
  <div class="f-col" style="left:301px"><h6>About Company</h6>
    <ul><li>Terms of Use</li><li>Terms &amp; Condition</li><li>News</li><li>Support</li><li>Contact Us</li><li>FAQ</li></ul></div>
  <div class="f-col" style="left:537px;width:290px"><h6>Contact Us</h6>
    <div class="contact-item"><svg width="12" height="16" viewBox="0 0 12 16"><path d="M6 0a6 6 0 00-6 6c0 4.5 6 10 6 10s6-5.5 6-10a6 6 0 00-6-6z" fill="#00AB8E"/><circle cx="6" cy="6" r="2" fill="#0b0b0b"/></svg><div><b>Location</b>241,Lorem ipsum dolor sited<br>Consectetur adipiscing elited</div></div>
    <div class="contact-item"><svg width="13" height="13" viewBox="0 0 24 24"><path d="M6.6 10.8a15 15 0 006.6 6.6l2.2-2.2c.3-.3.7-.4 1-.2 1.1.4 2.3.6 3.6.6.6 0 1 .4 1 1V20c0 .6-.4 1-1 1A17 17 0 013 4c0-.6.4-1 1-1h3.5c.6 0 1 .4 1 1 0 1.3.2 2.5.6 3.6.1.3 0 .7-.2 1z" fill="#00AB8E"/></svg><div><b>Phone</b>+1 888 888 8888</div></div>
    <div class="contact-item"><svg width="14" height="11" viewBox="0 0 14 11"><rect width="14" height="11" rx="1" fill="#00AB8E"/><path d="M1 1l6 5 6-5" stroke="#0b0b0b" fill="none"/></svg><div><b>Email</b>info@ashbrookcoating.com</div></div>
  </div>
  <div class="f-col" style="left:854px;width:240px"><h6>Stil have questios?</h6>
    <p style="margin-top:20px;font-size:12.5px;line-height:19px">Contact us using this form. A repesenta-tive will aswer your questions as soon as possible.</p>
    <span class="f-quote">GET A QUOTE</span></div>
  <div class="to-top"><svg width="14" height="14" viewBox="0 0 14 14"><path d="M3 9l4-4 4 4" stroke="#fff" stroke-width="2" fill="none"/></svg></div>
  <div class="f-line"></div>
  <div class="copyright">2023 Copyright -Ashbrook Coating Contractors, LLC &nbsp;| All Rights Reserved</div>
</footer>

</body>
</html>
```